依頼詳細
<使用してもらいたい文言:パターン①>
・マウスピース矯正クリアフィット治療実績2197症例
・北海道No1の症例数(2019,2020,2021年)
<使用してもらいたい文言:パターン②>
・透明で目立たないマウスピース矯正
・頭金0円、月々払いで10800円~
・矯正相談、オンライン相談も受付可能
サイトURL
http://moriyama-kyousei-example.com/
ページ数
1ページ
希望イメージ
シンプル 複雑
単色 カラフル
暗い 明るい
日常 高級
遊び心 厳粛
未来的 伝統的
女性的 男性的
希望する色
赤系、黄・オレンジ系、水色系
納品ファイル
• 高解像度JPG (.jpg)
補足説明
デザイン参考サイトは添付しています
PC版だけでなくスマホ版の作成もお願いします。
8〜9割はスマホからのアクセスなので、スマホ版のメインビジュアルを一番重要視しています。
スマホ版のサイズですが、添付画像の赤枠内に入るようなビジュアルでお願いします。

参考にもう一つのメインビジュアルの画像を添付します。

<使用してもらいたい文言:パターン③>
・オンライン診療で6ヶ月に1回の通院からOK
・他院で断られた方もOK
・スピード矯正で3ヶ月で綺麗な前歯に
■ 選んだ理由

当院の強みについての訴求がしっかりとできていた。

■ 提案者全員のお礼・コメント

良い提案をしていただいた方が3名ほどいらっしゃいました。そちらの方を当選と次点とさせていただきました。
今後もこのような機会があると思いますので、みなさま今後ともよろしくお願いいたします。

```html
<!DOCTYPE html>
<html lang="ja">
<head>
<meta charset="UTF-8">
<title>もりやま歯科 マウスピース矯正サイト</title>
<link rel="stylesheet" href="https://fonts.googleapis.com/css2?family=Noto+Sans+JP:wght@400;500;700;900&family=Noto+Serif+JP:wght@700;900&display=swap">
<style>
:root{
  --orange:#e8891c;
  --gold:#c4923a;
  --gold-light:#e0b86a;
  --ink:#222222;
  --grey-text:#5a5a5a;
  --beige-1:#f6ede2;
  --beige-2:#e9d8c3;
  --yellow:#f5b400;
  --blue:#2e9ad8;
  --red:#c8281e;
  --bar:#d6d6d6;
  --white:#ffffff;
  --black:#141414;
}
*{margin:0;padding:0;box-sizing:border-box;}
html,body{width:1200px;height:2596px;overflow:hidden;background:var(--white);}
body{font-family:"Noto Sans JP",sans-serif;color:var(--ink);}
.page{position:relative;width:1200px;height:2596px;overflow:hidden;}

/* header */
.site-header{position:absolute;left:0;top:0;width:1200px;height:160px;background:var(--white);}
.brand{position:absolute;left:160px;top:12px;text-align:center;width:740px;white-space:nowrap;}
.brand-name{display:flex;align-items:center;justify-content:center;gap:16px;font-size:56px;font-weight:900;color:var(--orange);line-height:1.15;}
.brand-dot{width:24px;height:24px;border-radius:50%;background:var(--orange);}
.brand-sub{font-size:50px;font-weight:700;color:var(--ink);line-height:1.25;letter-spacing:1px;}
.header-btn{position:absolute;top:20px;width:130px;height:130px;display:flex;align-items:center;justify-content:center;}
.header-btn.tel{left:930px;background:var(--yellow);}
.header-btn.menu{left:1062px;background:var(--blue);}

/* hero */
.hero{position:absolute;left:0;top:160px;width:1200px;height:1400px;background:linear-gradient(180deg,var(--beige-1),var(--beige-2));overflow:hidden;}
.hero-photo{position:absolute;left:470px;top:0;width:730px;height:1400px;background:radial-gradient(ellipse at 55% 35%,#f3ddcc 0%,#e8cdb6 45%,#dcc3a6 100%);}
.hero-lead{position:absolute;left:40px;top:330px;padding:14px 40px;background:var(--white);font-size:62px;font-weight:700;letter-spacing:4px;box-shadow:0 6px 18px rgba(0,0,0,.08);white-space:nowrap;}
.hero-title{position:absolute;left:40px;top:480px;font-size:104px;font-weight:900;letter-spacing:2px;line-height:1.1;white-space:nowrap;}
.hero-title em{font-style:normal;color:var(--orange);}
.hero-tag{position:absolute;left:170px;top:615px;font-size:28px;font-weight:500;letter-spacing:8px;color:var(--gold);white-space:nowrap;}
.down-badge{position:absolute;left:330px;top:690px;width:170px;height:170px;border-radius:50%;background:var(--orange);color:var(--white);display:flex;flex-direction:column;align-items:center;justify-content:center;font-weight:900;line-height:1;}
.down-badge small{font-size:30px;}
.down-badge b{font-size:64px;}
.monthly{position:absolute;left:60px;top:840px;font-size:56px;font-weight:700;}
.price{position:absolute;left:50px;top:910px;font-size:150px;font-weight:900;color:var(--gold);letter-spacing:-2px;line-height:1;white-space:nowrap;}
.price span{font-size:80px;}

/* ranking band */
.rank-band{position:absolute;left:0;top:1300px;width:1200px;height:230px;}
.rank-inner{position:absolute;left:0;top:0;width:1200px;height:200px;display:flex;align-items:center;justify-content:center;gap:26px;color:var(--white);white-space:nowrap;}
.rank-area{background:var(--white);color:var(--black);font-size:62px;font-weight:900;padding:4px 30px;border-radius:10px;letter-spacing:4px;}
.rank-no{font-family:"Noto Serif JP",serif;font-size:140px;font-weight:900;color:var(--gold-light);line-height:1;}
.rank-no small{font-size:76px;}
.rank-text{font-size:84px;font-weight:900;letter-spacing:4px;}
.rank-years{position:absolute;left:0;top:160px;width:1200px;text-align:center;font-size:24px;color:var(--gold-light);letter-spacing:3px;}

/* consult */
.consult{position:absolute;left:0;top:1560px;width:1200px;height:740px;background:var(--white);}
.consult-person{position:absolute;left:40px;top:120px;width:300px;height:620px;background:linear-gradient(180deg,#f1e6dc,#dcdcdc);border-radius:150px 150px 0 0;}
.consult-icons{position:absolute;left:520px;top:150px;display:flex;gap:200px;}
.consult-icon{width:96px;height:96px;border:4px solid var(--gold);border-radius:50%;display:flex;align-items:center;justify-content:center;}
.consult-main{position:absolute;left:390px;top:300px;font-size:56px;font-weight:500;color:var(--grey-text);letter-spacing:2px;white-space:nowrap;}
.consult-sub{position:absolute;left:390px;top:410px;font-size:64px;font-weight:700;color:var(--orange);letter-spacing:4px;border-bottom:6px dotted var(--orange);padding-bottom:10px;white-space:nowrap;}

/* fixed action bar */
.action-bar{position:absolute;left:0;top:2300px;width:1200px;height:296px;background:var(--bar);}
.tel-btn{position:absolute;left:20px;top:40px;width:710px;height:210px;display:flex;border-radius:16px;overflow:hidden;box-shadow:0 4px 10px rgba(0,0,0,.15);}
.tel-btn-icon{width:150px;background:var(--blue);display:flex;align-items:center;justify-content:center;}
.tel-btn-body{flex:1;background:var(--white);display:flex;flex-direction:column;justify-content:center;padding-left:34px;white-space:nowrap;}
.tel-btn-label{font-size:36px;color:var(--grey-text);font-weight:500;}
.tel-btn-number{font-size:64px;font-weight:900;color:var(--red);letter-spacing:1px;line-height:1.2;}
.web-btn{position:absolute;left:750px;top:40px;width:300px;height:210px;background:var(--white);border-radius:16px;display:flex;align-items:center;justify-content:center;font-size:48px;font-weight:500;color:var(--grey-text);box-shadow:0 4px 10px rgba(0,0,0,.15);}
.top-btn{position:absolute;left:1070px;top:80px;width:110px;height:130px;background:#8c8c8c;display:flex;align-items:center;justify-content:center;}
</style>
</head>
<body>
<div class="page">

  <header class="site-header">
    <div class="brand">
      <div class="brand-name"><span class="brand-dot"></span>もりやま歯科<span class="brand-dot"></span></div>
      <div class="brand-sub">マウスピース矯正サイト</div>
    </div>
    <div class="header-btn tel" aria-label="電話">
      <svg width="64" height="64" viewBox="0 0 24 24"><path fill="#fff" d="M6.6 10.8a15.2 15.2 0 0 0 6.6 6.6l2.2-2.2a1 1 0 0 1 1-.25 11.4 11.4 0 0 0 3.6.57 1 1 0 0 1 1 1V20a1 1 0 0 1-1 1A17 17 0 0 1 3 4a1 1 0 0 1 1-1h3.5a1 1 0 0 1 1 1c0 1.25.2 2.450.57 3.57a1 1 0 0 1-.25 1z"/></svg>
    </div>
    <div class="header-btn menu" aria-label="メニュー">
      <svg width="64" height="54" viewBox="0 0 64 54"><rect y="0" width="64" height="8" fill="#fff"/><rect y="23" width="64" height="8" fill="#fff"/><rect y="46" width="64" height="8" fill="#fff"/></svg>
    </div>
  </header>

  <section class="hero">
    <div class="hero-photo" role="img" aria-label="マウスピース矯正で笑顔を見せる女性の写真"></div>
    <div class="hero-lead">透明で目立たない</div>
    <h1 class="hero-title">マウスピース<em>矯正</em></h1>
    <div class="hero-tag">— MOUTHPIECE —</div>
    <div class="down-badge"><small>頭金</small><b>0円</b></div>
    <div class="monthly">月々払い</div>
    <div class="price">10,800<span>円〜</span></div>
  </section>

  <div class="rank-band">
    <svg width="1200" height="230" viewBox="0 0 1200 230" style="position:absolute;left:0;top:0">
      <polygon points="30,10 1170,10 1140,220 0,220" fill="#141414"/>
      <line x1="60" y1="30" x2="1140" y2="30" stroke="#c4923a" stroke-width="3"/>
      <line x1="40" y1="200" x2="1120" y2="200" stroke="#c4923a" stroke-width="3"/>
    </svg>
    <div class="rank-inner">
      <span class="rank-area">北海道</span>
      <span class="rank-no"><small>No.</small>1</span>
      <span class="rank-text">の症例数</span>
    </div>
    <div class="rank-years">(2019 / 2020 / 2021)</div>
  </div>

  <section class="consult">
    <div class="consult-person" role="img" aria-label="スマートフォンを持って案内するスタッフの写真"></div>
    <div class="consult-icons">
      <div class="consult-icon">
        <svg width="50" height="50" viewBox="0 0 24 24"><path fill="none" stroke="#c4923a" stroke-width="1.8" d="M7 3c-2.5 0-4 2-4 4.5 0 3 1.5 4.5 2 7.5.4 2.7 1 6 2.5 6s1.5-4 3-4h3c1.5 0 1.5 4 3 4s2.1-3.3 2.5-6c.5-3 2-4.5 2-7.5C21 5 19.5 3 17 3c-2 0-3 1-5 1S9 3 7 3z"/></svg>
      </div>
      <div class="consult-icon">
        <svg width="50" height="50" viewBox="0 0 24 24"><path fill="none" stroke="#c4923a" stroke-width="1.8" d="M4 4h16v11H9l-5 4z"/><circle cx="8.5" cy="9.5" r="1" fill="#c4923a"/><circle cx="12" cy="9.5" r="1" fill="#c4923a"/><circle cx="15.5" cy="9.5" r="1" fill="#c4923a"/></svg>
      </div>
    </div>
    <p class="consult-main">矯正相談・オンライン相談</p>
    <p class="consult-sub">どちらも受付可能です</p>
  </section>

  <nav class="action-bar">
    <div class="tel-btn">
      <div class="tel-btn-icon">
        <svg width="80" height="80" viewBox="0 0 24 24"><path fill="#fff" d="M6.6 10.8a15.2 15.2 0 0 0 6.6 6.6l2.2-2.2a1 1 0 0 1 1-.25 11.4 11.4 0 0 0 3.6.57 1 1 0 0 1 1 1V20a1 1 0 0 1-1 1A17 17 0 0 1 3 4a1 1 0 0 1 1-1h3.5a1 1 0 0 1 1 1c0 1.25.2 2.45.57 3.57a1 1 0 0 1-.25 1z"/></svg>
      </div>
      <div class="tel-btn-body">
        <span class="tel-btn-label">電話予約・問合せ</span>
        <span class="tel-btn-number">011-000-4821</span>
      </div>
    </div>
    <div class="web-btn">WEB予約</div>
    <div class="top-btn" aria-label="ページ上部へ">
      <svg width="60" height="60" viewBox="0 0 60 60"><polygon points="30,6 56,34 40,34 40,56 20,56 20,34 4,34" fill="#fff"/></svg>
    </div>
  </nav>

</div>
</body>
</html>
```